Business Card for By Karel Voss

Looking to have a business card designed for my lifestyle and fitness company. My company offers personal training, online programming and nutrition advice based out of London, United Kingdom.

I'd like to see modern, sleek designs, focusing on black, matte black or matte grey. Design doesn't need to be overly descriptive as this will also be used as a personal business card. I've included my logo.

Please note that my company is no longer called "Fitness by Karel Voss" but instead "By Karel Voss", this is because of my other ventures. Therefore please don't use the "fitness by karel voss" text.

information about my company can be found at www.bykarelvoss.com

Company is also based out of Leeds (United Kingdom) & Perth (Australia) this could be reflected on the card.

Industry/Entity Type

Business

Contact Information for Business Card

Karel Voss
+44 7382 615027
karel@bykarelvoss.com
www.bykarelvoss.com

Font styles to use
Sans Serif

Requirements
Must have
• All contact details and inclusion of my logo.

```html
<!DOCTYPE html>
<html lang="en">
<head>
<meta charset="utf-8">
<title>By Karel Voss — Business Card</title>
<link rel="stylesheet" href="https://fonts.googleapis.com/css2?family=Lato:wght@400&display=swap">
<style>
  :root {
    --page-bg: #d9dadc;
    --card-black: #060606;
    --card-back: #0b0b0c;
    --ink: #ffffff;
    --rule: #e6e6e6;
  }
  * { box-sizing: border-box; margin: 0; padding: 0; }
  html, body {
    width: 1200px; height: 1000px; overflow: hidden;
    background: var(--page-bg);
    font-family: "Lato", Arial, sans-serif;
    color: var(--ink);
  }
  .card {
    position: absolute; left: 220px;
    width: 760px; height: 434px;
    border-radius: 34px;
    overflow: hidden;
    box-shadow: 0 10px 24px rgba(0,0,0,.25);
  }
  .card--front { top: 44px; background: var(--card-black); }
  .card--back { top: 522px; background: var(--card-back); }

  .pattern-field {
    position: absolute; inset: 0;
    background: var(--card-black);
  }
  .front-brand {
    position: absolute; inset: 0;
    display: flex; align-items: center; justify-content: center; gap: 18px;
  }
  .brand-dot {
    width: 22px; height: 22px; border-radius: 50%; background: var(--ink); flex: none;
  }
  .brand-name {
    font-size: 52px; font-weight: 400; letter-spacing: 1px; color: var(--ink);
    white-space: nowrap;
  }

  .holder-name {
    position: absolute; left: 38px; top: 136px;
    font-size: 38px; font-weight: 400; line-height: 1.2;
  }
  .holder-rule {
    position: absolute; left: 38px; top: 210px;
    width: 388px; height: 2px; background: var(--rule);
  }
  .contact-list { position: absolute; left: 38px; top: 268px; list-style: none; }
  .contact-list li {
    display: flex; align-items: center; gap: 16px;
    font-size: 26px; height: 42px; white-space: nowrap;
  }
  .contact-list svg { width: 22px; height: 22px; fill: var(--ink); flex: none; }

  .back-brand {
    position: absolute; right: 40px; top: 110px; width: 240px;
    display: flex; flex-direction: column; align-items: center; gap: 14px;
  }
  .back-brand .brand-dot { width: 26px; height: 26px; }
  .back-brand .brand-name { font-size: 34px; }

  .site {
    position: absolute; right: 42px; top: 340px;
    font-size: 23px; white-space: nowrap;
  }
  .locations {
    position: absolute; right: 40px; top: 378px;
    font-size: 16.5px; white-space: nowrap;
  }
</style>
</head>
<body>
  <section class="card card--front" aria-label="Card front">
    <div class="pattern-field" role="img" aria-label="Repeating faint brand pattern on black"></div>
    <div class="front-brand">
      <span class="brand-dot"></span>
      <span class="brand-name">By Karel Voss</span>
    </div>
  </section>

  <section class="card card--back" aria-label="Card back">
    <h1 class="holder-name">Karel Voss</h1>
    <div class="holder-rule"></div>
    <ul class="contact-list">
      <li>
        <svg viewBox="0 0 24 24" aria-hidden="true"><path d="M6.6 10.8c1.4 2.8 3.8 5.1 6.6 6.6l2.2-2.2c.3-.3.7-.4 1-.2 1.1.4 2.3.6 3.6.6.6 0 1 .4 1 1V20c0 .6-.4 1-1 1C10.6 21 3 13.4 3 4c0-.6.4-1 1-1h3.5c.6 0 1 .4 1 1 0 1.3.2 2.5.6 3.6.1.3 0 .7-.2 1L6.6 10.8z"/></svg>
        <span>+44 7382 615027</span>
      </li>
      <li>
        <svg viewBox="0 0 24 24" aria-hidden="true"><path d="M2 5h20v14H2V5zm2 2v.2l8 5.6 8-5.6V7H4zm16 2.6-8 5.6-8-5.6V17h16V9.6z"/></svg>
        <span>karel@bykarelvoss.com</span>
      </li>
    </ul>
    <div class="back-brand">
      <span class="brand-dot"></span>
      <span class="brand-name">By Karel Voss</span>
    </div>
    <p class="site">www.bykarelvoss.com</p>
    <p class="locations">Leeds (United Kingdom) &amp; Perth (Australia)</p>
  </section>
</body>
</html>
```